Summit Builders Web Site / Business Cards

Construction Company that specializes in Water and Fire Damage, Residential ReModels, Landscaping and Building ADU (Accessory Dwelling Unit)

Growing and changing families often need additional space, and a remodeling project can often provide that. Adding a new area, or repurposing an existing one can satisfy this requirement.

Other times, homeowners want to update the look in their kitchen or bathroom with more than just a change of cabinetry or vanity doors and drawers. Whatever your needs are, Summit Builders has skilled workers who are bonded and insured, and ready to make your dreams and visions a reality.

Target Market(s)

Home Owners

Industry/Entity Type

Construction Company

Contact Information for Business Card

Center Logo with our information on the corners

Back side to be Logo Only
Contact Info
CSLB License # 4829516
info@summitbuildersca.example
www.summitbuildersca.example

Coding

Coded - Design and coding required

Number of Pages Required

5+ page

Font styles to use
Serif
Sans Serif

Requirements
Must have
• Using our Logo Colors
Home
About Us
Services
Projects / Portfolio
Contact Us
Nice to have
• Colors matching our Logo
Should not have
• Black because it doesnt match our logo

```html
<!DOCTYPE html>
<html lang="en">
<head>
<meta charset="utf-8">
<title>Summit Builders</title>
<link rel="stylesheet" href="https://fonts.googleapis.com/css2?family=Montserrat:wght@300;400;600;700;800&family=Work+Sans:wght@400;500;600&display=swap">
<style>
:root{
  --orange:#ff6a13;
  --orange-deep:#f2570a;
  --orange-soft:#ff8a3d;
  --ink:#1f1b19;
  --text:#2b2624;
  --white:#ffffff;
  --sky:#2a3a57;
  --sky-deep:#1a2438;
  --bar:#2a2523;
  --rule:#cfcfcf;
}
*{margin:0;padding:0;box-sizing:border-box}
html,body{width:1200px;height:3068px;overflow:hidden;background:var(--white)}
body{position:relative;font-family:"Work Sans",sans-serif;color:var(--text)}
.abs{position:absolute}
.center{text-align:center}

/* Hero */
.hero{position:absolute;left:0;top:0;width:1200px;height:660px;
  background:linear-gradient(160deg,#3b4c6b 0%,var(--sky) 40%,#5a4a3e 75%,#6b5a48 100%)}
.hero-slant{position:absolute;left:0;top:560px;width:1200px;height:110px}
.brand{position:absolute;left:157px;top:28px;color:var(--white);font-family:"Montserrat",sans-serif;font-weight:700;font-size:22px;letter-spacing:2px;line-height:1;display:flex;align-items:center;gap:10px}
.brand-mark{width:14px;height:14px;background:var(--orange)}
.nav{position:absolute;top:49px;left:0;font-family:"Work Sans",sans-serif;font-size:12px;color:var(--white)}
.nav a{position:absolute;color:var(--white);text-decoration:none;white-space:nowrap}
.nav-sep{position:absolute;left:870px;top:-1px;color:var(--white);font-size:12px}
.btn{position:absolute;background:var(--orange);color:var(--white);display:flex;align-items:center;justify-content:center;font-size:12px;font-family:"Work Sans",sans-serif;text-decoration:none}
.hero-title{position:absolute;left:0;width:1200px;text-align:center;color:var(--white);font-family:"Montserrat",sans-serif}
.hero-title.big{top:225px;font-weight:800;font-size:80px;line-height:1;letter-spacing:-1px}
.hero-title.light{top:305px;font-weight:300;font-size:56px;line-height:1;letter-spacing:1px}
.hero-tag{position:absolute;top:370px;left:0;width:1200px;text-align:center;color:var(--white);font-family:"Montserrat",sans-serif;font-size:16px;letter-spacing:4px}

/* About */
.eyebrow{font-family:"Work Sans",sans-serif;font-size:16px;color:var(--ink)}
.section-title{font-family:"Montserrat",sans-serif;font-weight:700;font-size:33px;letter-spacing:5px;color:var(--ink)}
.about-copy{position:absolute;left:161px;top:778px;width:440px;font-size:11.5px;line-height:24px;color:var(--ink)}
.about-copy p+p{margin-top:24px}
.about-photo{position:absolute;left:658px;top:681px;width:366px;height:360px;
  clip-path:polygon(50% 0,100% 30%,100% 100%,0 100%,0 30%);
  background:linear-gradient(180deg,#4a78b8 0%,#7aa3d6 45%,#c9a878 75%,#6b5236 100%)}

/* Stats */
.stat{position:absolute;display:flex;flex-direction:column;align-items:center;color:var(--white)}
.stat-num{font-family:"Montserrat",sans-serif;font-weight:300;font-size:40px;line-height:1}
.stat-label{font-family:"Montserrat",sans-serif;font-weight:700;font-size:19px;line-height:24px;text-align:center;margin-top:22px}
.stat-dark{background:linear-gradient(160deg,#3a3836,#242221)}
.stat-orange{background:linear-gradient(160deg,var(--orange-soft),var(--orange))}

/* Services */
.services{position:absolute;left:0;top:1399px;width:1200px;height:672px;
  background:linear-gradient(180deg,var(--orange) 0%,#ff7a26 50%,var(--orange-deep) 100%);
  clip-path:polygon(0 0,100% 41px,100% 607px,0 672px)}
.services .white{color:var(--white)}
.svc-col{position:absolute;top:1705px;width:280px;text-align:center;color:var(--white)}
.svc-col h3{font-family:"Montserrat",sans-serif;font-weight:600;font-size:20px;margin-top:22px}
.svc-col p{font-size:11.5px;line-height:21px;margin-top:20px}
.svc-col a{display:inline-block;margin-top:14px;font-size:11.5px;color:var(--white);font-style:italic;text-decoration:underline}
.svc-divider{position:absolute;top:1690px;width:1px;height:262px;background:rgba(255,255,255,.45)}

/* Projects */
.proj{position:absolute;overflow:hidden}
.proj-photo{width:100%;height:100%}
.proj-caption{position:absolute;left:0;bottom:0;width:100%;background:rgba(255,106,19,.85);color:var(--white);display:flex;align-items:center;gap:10px}
.proj-caption strong{font-family:"Montserrat",sans-serif;font-weight:700;letter-spacing:3px}
.proj-caption span{font-size:10px}

/* Newsletter */
.newsletter{position:absolute;left:0;top:2717px;width:1200px;height:54px;background:var(--bar)}
.news-label{position:absolute;left:200px;top:18px;color:var(--white);font-family:"Montserrat",sans-serif;font-weight:600;font-size:15px;letter-spacing:3px}
.news-icon{position:absolute;left:157px;top:12px;width:30px;height:30px;border-radius:50%;background:var(--white)}
.news-input{position:absolute;left:600px;top:7px;width:346px;height:40px;background:var(--white);font-size:9px;color:#aaa;padding:15px 14px}

/* Footer */
.foot-brand{position:absolute;left:182px;top:2850px;width:206px;display:flex;align-items:center;justify-content:center;gap:10px;font-family:"Montserrat",sans-serif;font-weight:700;font-size:20px;letter-spacing:2px;color:var(--orange)}
.foot-brand i{width:16px;height:16px;background:var(--orange);display:block}
.social{position:absolute;top:3015px;width:30px;height:30px;border-radius:50%;background:#2f6fb5}
.foot-h{position:absolute;top:2800px;font-family:"Montserrat",sans-serif;font-weight:600;font-size:19px;letter-spacing:3px;color:var(--ink)}
.foot-list{position:absolute;top:2856px;list-style:none;font-size:10px;color:var(--ink)}
.foot-list li{height:26.5px;display:flex;align-items:center;gap:8px}
.foot-list li::before{content:"\2714";font-size:8px}
.contact-list li::before{content:none}
.foot-rule{position:absolute;left:455px;top:3000px;width:602px;height:1px;background:var(--rule)}
.copyright{position:absolute;right:145px;top:3026px;font-size:10px;color:var(--ink)}
</style>
</head>
<body>

<header class="hero" role="img" aria-label="Photo of a builder in a hard hat hammering roof framing against the sky"></header>
<svg class="hero-slant" viewBox="0 0 1200 110" width="1200" height="110" aria-hidden="true">
  <polygon points="0,5 1200,85 1200,110 0,110" fill="#ffffff"/>
  <polygon points="0,0 1200,78 1200,95 0,8" fill="#ff6a13"/>
</svg>

<div class="brand"><span class="brand-mark"></span>SUMMIT BUILDERS</div>
<nav class="nav">
  <a style="left:530px">Home</a>
  <a style="left:607px">About Us</a>
  <a style="left:702px">Services</a>
  <a style="left:790px">Our Projects</a>
</nav>
<span class="nav-sep" style="top:48px">|</span>
<svg class="abs" style="left:886px;top:49px" width="18" height="18" viewBox="0 0 18 18" aria-hidden="true"><circle cx="7.5" cy="7.5" r="6" fill="none" stroke="#fff" stroke-width="1.4"/><line x1="12" y1="12" x2="17" y2="17" stroke="#fff" stroke-width="1.4"/></svg>
<a class="btn" style="left:921px;top:38px;width:130px;height:39px">CONTACT US</a>

<h1 class="hero-title big">SUMMIT</h1>
<div class="hero-title light">BUILDERS</div>
<div class="hero-tag">THE BEST CHOOSE US Because We Deliver</div>
<a class="btn" style="left:536px;top:408px;width:128px;height:40px">Learn More</a>
<svg class="abs" style="left:590px;top:498px" width="20" height="42" viewBox="0 0 20 42" aria-hidden="true">
  <rect x="4" y="1" width="12" height="19" rx="6" fill="none" stroke="#fff" stroke-width="1.5"/>
  <line x1="10" y1="5" x2="10" y2="9" stroke="#fff" stroke-width="1.5"/>
  <polyline points="5,26 10,31 15,26" fill="none" stroke="#fff" stroke-width="1.5"/>
  <polyline points="5,33 10,38 15,33" fill="none" stroke="#fff" stroke-width="1.5"/>
</svg>

<!-- About -->
<div class="abs eyebrow" style="left:161px;top:679px">ABOUT</div>
<h2 class="abs section-title" style="left:161px;top:706px">SUMMIT BUILDERS</h2>
<div class="about-copy">
  <p>Construction Company that specializes in Water and Fire Damage, Residential ReModels, Landscaping and Building ADU (Accessory Dwelling Unit) Growing and changing families often need additional space, and a remodeling project can often provide that. Adding a new area, or repurposing an existing one can satisfy this requirement.</p>
  <p>Other times, homeowners want to update the look in their kitchen or bathroom with more than just a change of cabinetry or vanity doors and drawers. Whatever your needs are, Summit Builders has skilled workers who are bonded and</p>
</div>
<a class="btn" style="left:162px;top:1013px;width:128px;height:39px">Learn More</a>
<div class="about-photo" role="img" aria-label="Builder carrying a hammer beside timber framing, set in a house-shaped frame"></div>

<!-- Stats -->
<div class="stat stat-dark" style="left:144px;top:1124px;width:300px;height:209px;padding-top:46px" role="img" aria-label="Completed modern house at dusk">
  <div class="stat-num">53</div><div class="stat-label">TOTAL<br>PROJECTS</div>
</div>
<div class="stat stat-orange" style="left:444px;top:1119px;width:312px;height:219px;padding-top:51px" role="img" aria-label="Crew in hard hats on site">
  <div class="stat-num">15</div><div class="stat-label">WORKING IN<br>STATES</div>
</div>
<div class="stat stat-dark" style="left:756px;top:1124px;width:300px;height:209px;padding-top:44px" role="img" aria-label="Workers in safety vests on site">
  <div class="stat-num">2,600</div><div class="stat-label">HOURS FOR<br>WORK</div>
</div>

<!-- Services -->
<section class="services" role="img" aria-label="Carpenters at work, tinted orange"></section>
<div class="abs eyebrow white center" style="left:0;top:1501px;width:1200px;color:#fff">OUR SERVICES</div>
<h2 class="abs section-title center" style="left:0;top:1528px;width:1200px;color:#fff">WHAT STAGE IS YOUR BUILDING?</h2>
<p class="abs center" style="left:200px;top:1587px;width:800px;font-size:11.5px;line-height:22px;color:#fff">Ut at neque blandit, hendrerit massa et, sodales ipsum. Sed eget urna tempor, porttitor leo et, interdum ex. Aenean sodales eros id rutrum tempus. Aenean in nisl sem. Sed interdum, felis vitae ultrices cursus, neque libero vestibulum neque,</p>

<div class="svc-col" style="left:141px">
  <svg width="46" height="46" viewBox="0 0 46 46" aria-hidden="true"><g fill="none" stroke="#fff" stroke-width="2"><polyline points="4,24 23,8 42,24"/><rect x="9" y="22" width="28" height="20"/><rect x="19" y="30" width="8" height="12"/><path d="M14 10c0-4 4-5 3-9M30 10c0-4 4-5 3-9"/></g></svg>
  <h3>Water and Fire Damage</h3>
  <p>Ut at neque blandit, hendrerit massa et, sodales ipsum. Sed eget urna tempor, porttitor leo et, interdum ex. Aenean</p>
  <a>Read More</a>
</div>
<div class="svc-divider" style="left:442px"></div>
<div class="svc-col" style="left:460px">
  <svg width="54" height="50" viewBox="0 0 54 50" aria-hidden="true"><g fill="none" stroke="#fff" stroke-width="3"><polyline points="3,26 27,4 51,26"/><polyline points="10,20 10,47 44,47 44,20"/><polyline points="21,47 21,30 33,30 33,47"/></g></svg>
  <h3>Residential ReModels</h3>
  <p>Aenean sodales eros id rutrum tempus. Aenean in nisl sem. Sed interdum, felis vitae ultrices cursus, neque libero vestibulum</p>
  <a>Read More</a>
</div>
<div class="svc-divider" style="left:755px"></div>
<div class="svc-col" style="left:773px">
  <svg width="50" height="54" viewBox="0 0 50 54" aria-hidden="true"><g fill="none" stroke="#fff" stroke-width="2"><rect x="3" y="3" width="26" height="49"/><rect x="29" y="18" width="18" height="34"/></g><g fill="#fff"><rect x="8" y="9" width="5" height="5"/><rect x="19" y="9" width="5" height="5"/><rect x="8" y="20" width="5" height="5"/><rect x="19" y="20" width="5" height="5"/><rect x="8" y="31" width="5" height="5"/><rect x="19" y="31" width="5" height="5"/><rect x="34" y="24" width="8" height="4"/><rect x="34" y="33" width="8" height="4"/><rect x="13" y="42" width="6" height="10"/></g></svg>
  <h3>Landscaping and Building</h3>
  <p>Ut at neque blandit, hendrerit massa et, sodales ipsum. Sed eget urna tempor, porttitor leo et, interdum ex.</p>
  <a>Read More</a>
</div>

<!-- Projects -->
<h2 class="abs section-title center" style="left:0;top:2122px;width:1200px">OUR PROJECTS</h2>
<p class="abs center" style="left:200px;top:2181px;width:800px;font-size:11.5px;line-height:23px;color:var(--ink)">Ut at neque blandit, hendrerit massa et, sodales ipsum. Sed eget urna tempor, porttitor leo et, interdum ex. Aenean sodales eros id rutrum tempus. Aenean in nisl sem. Sed interdum, felis vitae ultrices cursus</p>

<article class="proj" style="left:0;top:2312px;width:274px;height:313px">
  <div class="proj-photo" role="img" aria-label="Two-storey brick family home under blue sky" style="background:linear-gradient(180deg,#3f6fc4 0%,#8fb0e0 45%,#8a6a58 70%,#4c5a3a 100%)"></div>
  <div class="proj-caption" style="height:50px;padding-left:11px"><strong style="font-size:16px">Expansion</strong><span>|&nbsp;&nbsp;Los Angeles, CA</span></div>
</article>
<article class="proj" style="left:298px;top:2283px;width:603px;height:371px">
  <div class="proj-photo" role="img" aria-label="Modern high school building with curved stone facade and glass wing" style="background:linear-gradient(120deg,#e4dccd 0%,#d8cfbf 45%,#3f7fc9 60%,#8fb6e4 100%)"></div>
  <div class="proj-caption" style="height:61px;padding-left:42px"><strong style="font-size:19px">Title Here</strong><span>|&nbsp;&nbsp;State Here</span></div>
</article>
<article class="proj" style="left:925px;top:2312px;width:275px;height:313px">
  <div class="proj-photo" role="img" aria-label="Suburban house with lit garage at dusk" style="background:linear-gradient(180deg,#5e6fa8 0%,#b7a9c8 40%,#e0c6b4 60%,#6e7282 100%)"></div>
  <div class="proj-caption" style="height:50px;padding-left:23px"><strong style="font-size:16px">Title Here</strong><span>|&nbsp;&nbsp;Las Vegas, NV</span></div>
</article>

<!-- Newsletter -->
<div class="newsletter">
  <div class="news-icon"></div>
  <svg class="abs" style="left:164px;top:19px" width="16" height="16" viewBox="0 0 16 16" aria-hidden="true"><polygon points="2,7 14,2 9,14 8,8" fill="none" stroke="#ff6a13" stroke-width="1.3"/></svg>
  <div class="news-label">Subscribe To Newsletter</div>
  <div class="news-input">Send a Message...</div>
  <a class="btn" style="left:955px;top:7px;width:101px;height:40px;font-weight:600;font-size:13px;gap:10px">Send <span>&#10230;</span></a>
</div>

<!-- Footer -->
<div class="foot-brand"><i></i>SUMMIT BUILDERS</div>
<span class="social" style="left:230px"></span>
<span class="social" style="left:271px;background:#3aa3e0"></span>
<span class="social" style="left:311px;background:#1f78b4"></span>

<h3 class="foot-h" style="left:464px">Services</h3>
<ul class="foot-list" style="left:464px">
  <li>Water and Fire Damage</li><li>Residential ReModels</li><li>Landscaping and Building ADU</li>
</ul>
<h3 class="foot-h" style="left:689px">Site Map</h3>
<ul class="foot-list" style="left:689px">
  <li>Home</li><li>About Us</li><li>Services</li><li>Our Projects</li><li>Contact Us</li>
</ul>
<h3 class="foot-h" style="left:882px">Get In Touch</h3>
<ul class="foot-list contact-list" style="left:892px">
  <li><svg width="14" height="14" viewBox="0 0 14 14" aria-hidden="true"><path d="M3 1l3 3-2 2c1 2 2 3 4 4l2-2 3 3-2 2C6 13 1 8 1 3z" fill="none" stroke="#555" stroke-width="1"/></svg>+1 555 014 2290</li>
  <li style="margin-top:10px"><svg width="14" height="10" viewBox="0 0 14 10" aria-hidden="true"><rect x=".5" y=".5" width="13" height="9" fill="none" stroke="#555"/><polyline points=".5,.5 7,6 13.5,.5" fill="none" stroke="#555"/></svg>info@summitbuildersca.example</li>
</ul>
<div class="foot-rule"></div>
<div class="copyright">© 2020 SUMMIT BUILDERS - ALL RIGHTS RESERVED.</div>

</body>
</html>
```